Granite, Zinc and Clay Roofing LLC needs a new business card

I need a new business card because I have a new address.
I do slate copper and tile roofs. My webpage is: www.granitezincandclayroofing.example

```html
<!DOCTYPE html>
<html lang="en">
<head>
<meta charset="utf-8">
<title>Granite, Zinc and Clay Roofing – Business Card</title>
<link href="https://fonts.googleapis.com/css2?family=Poppins:wght@400;500;600&display=swap" rel="stylesheet">
<style>
  :root {
    --backdrop: #c8c5c3;
    --card-black: #1b1b1c;
    --sky-blue: #5a9cc8;
    --band-blue: #5a9bc6;
    --ink-dark: #121416;
    --text-light: #f2f2f2;
  }
  html, body {
    margin: 0;
    width: 1200px;
    height: 1200px;
    overflow: hidden;
    background: var(--backdrop);
    font-family: "Poppins", sans-serif;
  }
  .card {
    position: absolute;
    left: 243px;
    width: 702px;
    height: 400px;
    border-radius: 22px;
    background: var(--card-black);
    overflow: hidden;
    box-shadow: 0 6px 14px rgba(0,0,0,0.35);
  }
  .card-front { top: 170px; }
  .card-back { top: 630px; }

  .front-name {
    position: absolute;
    top: 150px;
    left: 0;
    width: 100%;
    text-align: center;
    color: var(--sky-blue);
    font-weight: 500;
    font-size: 26px;
    line-height: 1.25;
    letter-spacing: 0.5px;
  }
  .call-label {
    position: absolute;
    top: 302px;
    width: 100%;
    text-align: center;
    color: var(--sky-blue);
    font-weight: 500;
    font-size: 16px;
    letter-spacing: 1px;
  }
  .call-number {
    position: absolute;
    top: 328px;
    width: 100%;
    display: flex;
    justify-content: center;
    align-items: center;
    gap: 6px;
    color: var(--text-light);
    font-size: 16px;
    letter-spacing: 0.8px;
  }
  .call-number svg { width: 18px; height: 18px; }

  .owner-name {
    position: absolute;
    top: 22px;
    left: 25px;
    margin: 0;
    color: var(--text-light);
    font-weight: 600;
    font-size: 21px;
  }
  .owner-role {
    position: absolute;
    top: 53px;
    left: 25px;
    color: var(--text-light);
    font-size: 15px;
    letter-spacing: 1.5px;
  }
  .info-band {
    position: absolute;
    left: 0;
    top: 252px;
    width: 100%;
    height: 148px;
    background: var(--band-blue);
  }
  .address {
    position: absolute;
    top: 16px;
    left: 25px;
    color: var(--ink-dark);
    font-weight: 500;
    font-size: 19px;
    line-height: 24px;
  }
  .contact-line {
    position: absolute;
    left: 25px;
    display: flex;
    align-items: center;
    gap: 9px;
    color: var(--ink-dark);
    font-weight: 500;
    font-size: 16px;
  }
  .contact-line svg { width: 16px; height: 16px; }
  .contact-web { top: 74px; }
  .contact-mail { top: 100px; }
  .band-name {
    position: absolute;
    right: 30px;
    top: 44px;
    width: 230px;
    text-align: right;
    color: var(--ink-dark);
    font-weight: 500;
    font-size: 20px;
    line-height: 1.25;
  }
</style>
</head>
<body>
  <section class="card card-front">
    <div class="front-name">Granite, Zinc &amp; Clay<br>Roofing</div>
    <div class="call-label">Call Us Now</div>
    <div class="call-number">
      <svg viewBox="0 0 24 24" aria-hidden="true"><path fill="#111" d="M6.6 10.8c1.4 2.8 3.8 5.1 6.6 6.6l2.2-2.2c.3-.3.7-.4 1-.2 1.1.4 2.3.6 3.6.6.6 0 1 .4 1 1V20c0 .6-.4 1-1 1C10.6 21 3 13.4 3 4c0-.6.4-1 1-1h3.5c.6 0 1 .4 1 1 0 1.3.2 2.5.6 3.6.1.3 0 .7-.2 1l-2.3 2.2z"/></svg>
      <span>(440) 555 0187</span>
    </div>
  </section>

  <section class="card card-back">
    <h1 class="owner-name">Marek (Mark) Halden</h1>
    <div class="owner-role">Owner</div>
    <div class="info-band">
      <div class="address">2870 Orchard Rd,<br>Millbrook, OH 44099</div>
      <div class="contact-line contact-web">
        <svg viewBox="0 0 24 24" aria-hidden="true"><g fill="none" stroke="#121416" stroke-width="2"><circle cx="12" cy="12" r="9"/><path d="M3 12h18M12 3c3 3 3 15 0 18M12 3c-3 3-3 15 0 18"/></g></svg>
        <span>www.granitezincandclayroofing.example</span>
      </div>
      <div class="contact-line contact-mail">
        <svg viewBox="0 0 24 24" aria-hidden="true"><rect x="2" y="5" width="20" height="14" fill="#121416"/><path d="M2 5l10 8 10-8" fill="none" stroke="#5a9bc6" stroke-width="2"/></svg>
        <span>gzcroofingllc@mail.example</span>
      </div>
      <div class="band-name">Granite, Zinc &amp; Clay Roofing</div>
    </div>
  </section>
</body>
</html>
```